Die Verpackung soll zum Einzelversenden der Flasche dienen. Sie soll aber auch schön sein das diese Flasche inklusive der Verpackung auch im Supermarkt stehen kann. .
Zielgruppe
Wir sind eine Premium Gin-Marke mit einem Produkt. Unser Mossy7Rum. Mit 57 Prozent Navy Strength. London dry.
Alle informationen dazu gibt es auch auf der website. Einzige Änderung ist von den 4 Gründern mit denen wir gestartet haben sind 2 ausgeschieden. Unser Slogan ist grüssdenholzmann. Das ist die Felsformation des Karvendelgebirges vor unserer Haustüre.
Aufgabenstellung
Ci muss eingehalten werden. Alles was benötigt wird kann zur verfügung gestellt werden wie Schrift, logos usw.

```html
<!DOCTYPE html>
<html lang="de">
<head>
<meta charset="utf-8">
<title>Mossy7Rum – Etikett</title>
<link href="https://fonts.googleapis.com/css2?family=Questrial&family=Open+Sans:wght@700&display=swap" rel="stylesheet">
<style>
  :root {
    --page-bg: #f6f6f8;
    --panel-back: #0b1724;
    --panel-front: #2e3d4d;
    --band-blue: #1f3a4f;
    --gold: #c4b49a;
    --text-grey: #b3b3b3;
    --mountain-light: #a9abad;
    --mountain-mid: #7f8f97;
  }
  * { margin: 0; padding: 0; box-sizing: border-box; }
  html, body { width: 1200px; height: 1200px; overflow: hidden; background: var(--page-bg); }
  body { position: relative; font-family: "Questrial", sans-serif; }

  .label { position: absolute; left: 274px; top: 210px; width: 655px; height: 795px; }

  .panel-back {
    position: absolute; left: 0; top: 0; width: 329px; height: 100%;
    background: var(--panel-back);
  }
  .panel-front {
    position: absolute; left: 329px; top: 0; width: 326px; height: 100%;
    background: var(--panel-front);
  }

  .story {
    position: absolute; left: 50px; top: 64px; width: 226px;
    color: var(--text-grey); font-size: 11.2px; line-height: 19.9px;
    text-align: center; letter-spacing: 0.15px;
  }
  .story p + p { margin-top: 19.9px; }

  .maker {
    position: absolute; left: 0; width: 329px; top: 700px;
    color: var(--text-grey); font-size: 9.6px; line-height: 14px;
    text-align: center; letter-spacing: 0.2px;
  }

  .tagline {
    position: absolute; left: 0; width: 100%; top: 66px;
    color: var(--text-grey); font-size: 11.5px; text-align: center; letter-spacing: 0.3px;
  }

  .brand {
    position: absolute; left: 0; width: 100%; top: 440px;
    color: var(--gold); font-size: 46px; text-align: center; letter-spacing: 1px;
  }

  .landscape {
    position: absolute; left: 0; top: 490px; width: 100%; height: 86px;
    background: linear-gradient(180deg, var(--panel-front) 0%, var(--mountain-light) 20%, var(--mountain-mid) 55%, var(--band-blue) 100%);
  }

  .volume {
    position: absolute; left: 0; width: 100%; top: 740px;
    color: var(--text-grey); font-size: 11.6px; text-align: center; letter-spacing: 0.3px;
  }

  .band {
    position: absolute; left: 2px; top: 576px; width: 653px; height: 20px;
    background: var(--band-blue);
    border-top: 1.5px solid var(--gold); border-bottom: 1.5px solid var(--gold);
  }
  .band-text {
    position: absolute; left: 329px; width: 326px; top: 0; line-height: 17px;
    font-family: "Open Sans", sans-serif; font-weight: 700;
    color: var(--gold); font-size: 10px; text-align: center; letter-spacing: 0.2px;
  }
</style>
</head>
<body>
  <div class="label">
    <section class="panel-back">
      <div class="story">
        <p>Lorem ipsum dolor sit amet, consec-tetuer adipiscing elit, sed diam nonummy nibh euismod tincidunt ut laoreet dolore magna aliquam erat volutpat. Ut wisi enim ad minim veniam, quis nostrud exerci tation ullamcorper suscipit lobortis nisl ut aliquip ex ea commodo consequat.</p>
        <p>Duis autem vel eum iriure dolor in hendrerit in vulputate velit esse molestie consequat, vel illum dolore eu feugiat nulla facilisis at vero eros et accumsan et iusto odio dignissim qui blandit praesent luptatum zzril delenit augue duis dolore te feugait nulla facilisi.</p>
        <p>Lorem ipsum dolor sit amet, cons ectetuer adipiscing elit, sed diam nonummy nibh euismod tincidunt ut laoreet dolore magna aliquam erat</p>
      </div>
      <div class="maker">
        Hersteller:<br>
        7M Destillerie UG (haftungsbeschränkt) &amp; Co KG<br>
        Am Lindenhang 12<br>
        83999 Tannweiler
      </div>
    </section>

    <section class="panel-front">
      <div class="tagline">Ein kraftvoller und facettenreicher Gin</div>
      <div class="brand" style="top:395px;">Mossy7Rum</div>
      <div class="landscape" role="img" aria-label="Silhouette einer Bergkette mit Felsformation in Grau- und Blautönen"></div>
      <div class="volume">0,5 Liter - Vol. 57%</div>
    </section>

    <div class="band">
      <div class="band-text">-&nbsp; LONDON DRY GIN AUS TANNWEILER -</div>
    </div>
  </div>
</body>
</html>
```